Mellow Meadow

Hello,
I require the following to be completed for my business.
My company font is Spicy Rice, and I'm enclosing a picture of a logo.
Please amend the enclosed brochure to make it look better.(fieldgrovepamphlet6)
Please amend the enclosed installation guide, so it says my company name, addresses logo, etc on it (installation instructions).
Please create a letter head and business cards
My name is Tomas Verhundic and my title is National Sales Manager, company address is on the site: mellowmeadow.ca, tomas@mellowmeadow.ca cell phone is 416-295-6148, I'm thinking we have just the logo on one side and "Premium Synthetic Turf" in spicy font. On the letter head, on the bottom i'm thinking of showing grass come up, see my website.
The MM_ Label pages is required to create product labels, please add a colourmark of my company logo in the designs. (I'll require 6 or 8 per page, and more product are coming, let's just iron down layout. (my sites product page has more products)
Target Market(s)
The target market will be home owners.
Industry/Entity Type
Cell Phone
Logo Text
Design Build Innovate
Look and feel
Each slider illustrates characteristics of the customer's brand and the style your logo design should communicate.

```html
<!DOCTYPE html>
<html lang="en">
<head>
<meta charset="utf-8">
<title>Mellow Meadow Letterhead</title>
<link rel="stylesheet" href="https://fonts.googleapis.com/css2?family=Spicy+Rice&display=swap">
<style>
  :root {
    --paper: #ffffff;
    --frame: #8fc98a;
    --brand-green: #3f8f2f;
    --faint-green: #e4efd9;
    --grass-light: #6fbf45;
    --grass-mid: #3f9a2c;
    --grass-dark: #2a6e1e;
    --contact-text: #ffffff;
  }
  html, body {
    margin: 0;
    padding: 0;
    width: 849px;
    height: 1200px;
    overflow: hidden;
    background: var(--paper);
  }
  .letterhead {
    position: relative;
    width: 849px;
    height: 1200px;
    box-sizing: border-box;
    border: 3px solid var(--frame);
    background: var(--paper);
    overflow: hidden;
    font-family: "Spicy Rice", cursive;
  }
  .brand {
    position: absolute;
    left: 40px;
    top: 62px;
    display: flex;
    align-items: center;
    gap: 16px;
  }
  .brand-dot {
    width: 34px;
    height: 34px;
    border-radius: 50%;
    background: var(--brand-green);
  }
  .brand-name {
    font-size: 52px;
    color: var(--brand-green);
    line-height: 1;
  }
  .brand-faint {
    position: absolute;
    left: 0;
    right: 0;
    top: 570px;
    text-align: center;
    font-size: 82px;
    color: var(--faint-green);
    line-height: 1;
  }
  .grass-band {
    position: absolute;
    left: 0;
    right: 0;
    bottom: 0;
    height: 172px;
    background: linear-gradient(180deg, var(--grass-light) 0%, var(--grass-mid) 45%, var(--grass-dark) 100%);
  }
  .contact {
    position: absolute;
    left: 0;
    right: 0;
    bottom: 52px;
    text-align: center;
    color: var(--contact-text);
    font-size: 36px;
    line-height: 1.15;
    text-shadow: 0 2px 3px rgba(0,0,0,0.35);
  }
  .contact p { margin: 0; }
</style>
</head>
<body>
  <main class="letterhead">
    <header class="brand">
      <span class="brand-dot"></span>
      <span class="brand-name">Mellow Meadow</span>
    </header>

    <div class="brand-faint" aria-hidden="true">Mellow Meadow</div>

    <div class="grass-band" role="img" aria-label="Photograph of green synthetic turf grass rising along the bottom of the page"></div>

    <footer class="contact">
      <p>mellowmeadow.ca, tomas@mellowmeadow.ca</p>
      <p>cell phone 416-295-6148</p>
    </footer>
  </main>
</body>
</html>
```